KT Prime Motion personal training needs a new Business Card design for 2016

Business Card design:
Our current business card is very plain
We are bringing on our first team member next year and thought its a perfect time to have a new face lift for our company!

We are a Personal Training business "KT Prime Motion" who specializes in strength and conditioning / weightloss training,
We also run a yearly Bootcamp called "Ferocity Drillcamps", this is our Logo Design which we are looking for

The pink and blue in the logo are our business colours, how ever we don't want those colours to heavily dominate the card.

We are looking for a business card which is eye catching, and creative.

I am open to suggestions and any designs :)

Logo Design:

For our Logo Design we are looking for a bright, energetic logo, preferably a word logo which portrays strength and high intensity
If it has icon's etc in it thats fine again im open for suggestions :)
The Logo Design is for our Bootcamp which runs yearly
The bootcamp is called "Ferocity Drillcamp"

Target Market(s)

Age 20-40
Individuals who want to look great and have more energy

Industry/Entity Type

Business

Contact Information for Business Card

On the front
KT Prime Motion Doriel Maxton Personal Training / Bootcamps / Pilates / Nutrition Healthy mind, Healthy body, Ultimate lifestyle < our slogan
Icons for the following
Email:
Mobile:
Facebook:
Instagram:

On the back we would like to include somewhere
"Show this card to receive 50% off your first 30min pt session"
"Valid to one user only"

Logo Text

Ferocity Drillcamp

Font styles to use
Serif

Colors
e34197
0255a3
000000
ffffff

Requirements
Must have
• - Icons for instagram, facebook, email and mobile phone
• - Slogan: Healthy mind, Healthy body, Ultimate lifestyle
• - What we offer: Personal Training , Bootcamps, Pilates, Nutrition
• - Logo
• -
Nice to have
• - Our 50% offer on the back
• - a place for a photo
Should not have
• - Pink and Blue everywhere

```html
<!DOCTYPE html>
<html lang="en">
<head>
<meta charset="utf-8">
<title>KT Prime Motion – Business Cards</title>
<link rel="stylesheet" href="https://fonts.googleapis.com/css2?family=PT+Sans:wght@400;700&family=PT+Sans+Narrow:wght@700&display=swap">
<style>
  :root {
    --brand-pink: #e34197;
    --brand-blue: #0255a3;
    --ink: #000000;
    --paper: #ffffff;
    --backdrop: #ecebe8;
    --card-shadow: rgba(0, 0, 0, 0.18);
  }
  * { box-sizing: border-box; margin: 0; padding: 0; }
  html, body {
    width: 1200px;
    height: 900px;
    overflow: hidden;
    background: var(--backdrop);
    font-family: "PT Sans", sans-serif;
  }
  .canvas {
    position: relative;
    width: 1200px;
    height: 900px;
  }
  .card {
    position: absolute;
    width: 620px;
    height: 354px;
    background: var(--paper);
    box-shadow: 0 6px 18px var(--card-shadow);
    overflow: hidden;
  }
  .card--offer { left: 290px; top: 48px; }
  .card--contact { left: 290px; top: 498px; }

  /* Offer side */
  .offer-side {
    display: flex;
    flex-direction: column;
    align-items: center;
    text-align: center;
    padding-top: 34px;
  }
  .brand-mark {
    width: 52px;
    height: 52px;
    border-radius: 50%;
    background: var(--brand-blue);
    margin-bottom: 8px;
  }
  .brand-name {
    font-family: "PT Sans Narrow", sans-serif;
    font-weight: 700;
    color: var(--brand-blue);
    font-size: 40px;
    line-height: 1;
    letter-spacing: 0.5px;
    text-transform: uppercase;
  }
  .slogan {
    font-family: "PT Sans Narrow", sans-serif;
    font-weight: 700;
    color: var(--brand-pink);
    font-size: 13px;
    margin-top: 4px;
    word-spacing: 2px;
  }
  .offer-heading {
    color: var(--brand-blue);
    font-size: 18px;
    font-weight: 400;
    margin-top: 26px;
    text-transform: uppercase;
    letter-spacing: 0.5px;
  }
  .services {
    color: var(--brand-pink);
    font-size: 19px;
    margin-top: 4px;
    word-spacing: 3px;
  }
  .promo {
    color: var(--brand-blue);
    font-size: 18px;
    margin-top: 14px;
  }
  .promo-terms {
    color: var(--brand-pink);
    font-size: 17px;
    margin-top: 2px;
  }

  /* Contact side */
  .corner-accent {
    position: absolute;
    background: var(--brand-pink);
  }
  .corner-accent--top {
    left: 0; top: 10px;
    width: 170px; height: 120px;
    clip-path: polygon(0 20%, 45% 0, 100% 30%, 60% 100%, 0 85%);
  }
  .corner-accent--bottom {
    left: 90px; top: 220px;
    width: 210px; height: 134px;
    clip-path: polygon(0 45%, 50% 0, 100% 55%, 85% 100%, 10% 100%);
  }
  .contact-brand {
    position: absolute;
    right: 34px;
    top: 34px;
    text-align: left;
  }
  .contact-brand .brand-name { font-size: 38px; }
  .contact-brand .slogan { font-size: 12.5px; }
  .holder {
    position: absolute;
    left: 330px;
    top: 172px;
  }
  .holder-name {
    color: var(--brand-blue);
    font-size: 22px;
    margin-bottom: 8px;
  }
  .contact-list { list-style: none; }
  .contact-item {
    display: flex;
    align-items: center;
    gap: 12px;
    color: var(--brand-pink);
    font-size: 17px;
    line-height: 26px;
  }
  .contact-icon {
    width: 13px;
    height: 13px;
    flex: none;
    fill: var(--brand-blue);
  }
</style>
</head>
<body>
<main class="canvas">

  <section class="card card--offer">
    <div class="offer-side">
      <span class="brand-mark" aria-hidden="true"></span>
      <h1 class="brand-name">KT Prime Motion</h1>
      <p class="slogan">Strong Mind &nbsp;|&nbsp; Fit Body &nbsp;|&nbsp; Prime Living</p>
      <h2 class="offer-heading">What We Offer</h2>
      <p class="services">Personal Training &nbsp;| Bootcamps &nbsp;| &nbsp;Pilates &nbsp;| &nbsp;Nutrition</p>
      <p class="promo">Show this card to receive 50% off your first 30min pt session</p>
      <p class="promo-terms">Valid to one user only</p>
    </div>
  </section>

  <section class="card card--contact">
    <div class="corner-accent corner-accent--top" role="img" aria-label="Pink fitness equipment graphic"></div>
    <div class="corner-accent corner-accent--bottom" role="img" aria-label="Pink fitness equipment graphic"></div>

    <div class="contact-brand">
      <h2 class="brand-name">KT Prime Motion</h2>
      <p class="slogan">Strong Mind &nbsp;|&nbsp; Fit Body &nbsp;|&nbsp; Prime Living</p>
    </div>

    <div class="holder">
      <p class="holder-name">Doriel Maxton</p>
      <ul class="contact-list">
        <li class="contact-item">
          <svg class="contact-icon" viewBox="0 0 16 16" aria-label="Phone"><path d="M3.6 1l2.6 3-1.5 1.8c.9 2 2.5 3.6 4.5 4.5L11 8.8l3 2.6-1.4 2.8C7 14 2 9 1.8 3.4z"/></svg>
          555 014 2876
        </li>
        <li class="contact-item">
          <svg class="contact-icon" viewBox="0 0 16 16" aria-label="Email"><path d="M1 3h14v10H1z M2.5 4.5v.4L8 9l5.5-4.1v-.4z" fill-rule="evenodd"/></svg>
          hello@ktprimemotion.net
        </li>
        <li class="contact-item">
          <svg class="contact-icon" viewBox="0 0 16 16" aria-label="Social page"><path d="M2 2h12v9H7l-3.5 3v-3H2z"/></svg>
          ktprimemotion.social
        </li>
        <li class="contact-item">
          <svg class="contact-icon" viewBox="0 0 16 16" aria-label="Link"><path d="M6.5 9.5l3-3 1 1-3 3z M4.5 7.5l2-2a2.5 2.5 0 0 1 3.5 0l-1 1a1 1 0 0 0-1.5 0l-2 2a1 1 0 0 0 1.5 1.5l.5.5-.5.5a2.5 2.5 0 0 1-2.5-3.5z M11.5 8.5l-2 2a2.5 2.5 0 0 1-3.5 0l1-1a1 1 0 0 0 1.5 0l2-2a1 1 0 0 0-1.5-1.5l-.5-.5.5-.5a2.5 2.5 0 0 1 2.5 3.5z"/></svg>
          @ktprimemotion.train
        </li>
      </ul>
    </div>
  </section>

</main>
</body>
</html>
```